We need a redesign of our current website: www.halvardgroupsite.com. Halvard Group is a fully integrated hospitality development, management, and investment firm. We strive for leadership in each of our segments by building quality assets, exacting high standards of customer service, and focusing on returns for our investors and partners.

It is our mission to provide our guests an exceptional lodging experience; our clients an unsurpassed level of management in their properties; and create positive returns for our investors and partners. We achieve our mission via a company culture of transparency, ownership of our actions, and accountability for our results.

Target Market(s)

hotel owners, hotel developers, hotel investors, bankers

Industry/Entity Type

Hospitality

Requirements
Must have
• Our logo has to be there along with the quote and the ability to convey the following quote off of our current website: "Halvard was founded on the principles of integrity, honesty, loyalty, and trust. These convictions embody our company at every level, and show in every action."

```html
<!DOCTYPE html>
<html lang="en">
<head>
<meta charset="utf-8">
<title>Halvard Group – Hospitality Management</title>
<link rel="stylesheet" href="https://fonts.googleapis.com/css2?family=Noto+Sans:wght@400;700&family=Didact+Gothic&family=Kite+One&family=Comfortaa:wght@400&display=swap">
<style>
  :root{
    --orange:#f68b1f;
    --orange-light:#fbab3c;
    --orange-text:#e8801c;
    --brown:#7a6553;
    --ink:#2f2a26;
    --text:#3d3833;
    --muted:#6b5e54;
    --page-top:#f1f0ee;
    --peach:#fccb9d;
    --peach-box:#f6e4da;
    --footer:#3a3a3a;
    --white:#ffffff;
  }
  *{box-sizing:border-box;margin:0;padding:0}
  html,body{width:1200px;height:989px;overflow:hidden}
  body{font-family:"Noto Sans",sans-serif;color:var(--text);position:relative;
    background:linear-gradient(to bottom,var(--page-top) 0,#f3efeb 380px,#fbdcbc 583px)}
  .abs{position:absolute}

  /* navigation */
  .nav{position:absolute;left:0;top:0;width:1200px;height:46px;
    background:linear-gradient(to bottom,var(--orange-light),var(--orange));
    box-shadow:0 1px 3px rgba(0,0,0,.25)}
  .nav a{position:absolute;top:14px;font-size:15px;color:var(--white);text-decoration:none;letter-spacing:.3px}
  .nav .current{color:var(--ink);left:64px;top:4px;height:42px;width:76px;padding-top:10px;text-align:center;
    background:linear-gradient(to bottom,#fdb95a,#f99a2c);
    border-left:3px solid #e07d18;border-right:3px solid #e07d18}

  /* header */
  .brand{left:74px;top:70px;display:flex;align-items:center;gap:14px}
  .brand-mark{width:62px;height:62px;border-radius:50%;background:var(--orange)}
  .brand-name{font-family:"Comfortaa",sans-serif;font-size:28px;line-height:30px;color:var(--orange);letter-spacing:2px;text-transform:uppercase}
  .phone{left:909px;top:54px;display:flex;align-items:center;gap:14px;font-size:21px;color:var(--muted);letter-spacing:1px}

  /* feature slider */
  .feature-banner{left:55px;top:195px;width:575px;height:62px;background:var(--brown);
    clip-path:polygon(0 0,100% 0,100% 100%,0 100%,22px 50%)}
  .feature-title{left:100px;top:208px;font-family:"Didact Gothic",sans-serif;font-size:31px;color:var(--white);letter-spacing:.5px}
  .feature-text{left:103px;top:273px;width:482px;font-size:14px;line-height:19.6px;color:var(--text);text-align:justify}
  .btn-more{left:506px;top:393px;width:76px;height:33px;background:var(--orange);border:1px solid #5a3a1a;
    color:var(--ink);font-size:16px;font-weight:700;display:flex;align-items:center;justify-content:center;gap:6px}
  .slider-dots{left:101px;top:450px;display:flex;gap:8px}
  .slider-dots span{width:10px;height:10px;border-radius:50%;background:var(--orange)}
  .slider-dots span:first-child{background:var(--muted)}
  .feature-photo{left:629px;top:133px;width:488px;height:328px;border:5px solid #3b3b3b;
    background:linear-gradient(135deg,#c9a27a 0,#8a5a3a 40%,#5a3426 70%,#2e1f18 100%)}
  .photo-tab{left:1112px;top:193px;width:17px;height:64px;background:var(--brown);
    clip-path:polygon(0 0,100% 0,100% 88%,0 100%)}

  /* quote */
  .quote{left:60px;top:491px;width:1080px;text-align:center;font-family:"Kite One",sans-serif;font-size:19px;line-height:24px;color:var(--muted)}
  .quote strong{color:var(--ink);font-weight:400;font-size:21px}
  .quote-author{right:83px;top:552px;font-size:16px;color:var(--ink)}

  /* info band */
  .info-band{left:0;top:582px;width:1200px;height:237px;background:var(--peach);border-top:1px solid var(--orange)}
  .col-title{font-size:21px;color:#4a3f37;position:absolute;top:598px}
  .welcome-text{left:66px;top:630px;width:357px;font-size:14.3px;line-height:19.6px;text-align:justify}
  .link-more{font-size:14px;font-weight:700;color:var(--orange-text);position:absolute}
  .service-list{left:493px;top:638px;list-style:none}
  .service-list li{width:229px;height:27px;margin-bottom:12px;border:1px solid #5a4a40;background:var(--peach-box);
    font-size:14.5px;color:var(--ink);padding:3px 0 0 8px;display:flex;align-items:center;gap:6px}
  .news-item{left:823px;width:310px;font-size:14.3px;line-height:19.6px}
  .news-item h3{font-weight:400;color:#111;font-size:14.5px}
  .news-divider{left:823px;top:714px;width:296px;height:1px;background:var(--orange-text)}

  /* footer */
  .footer{left:0;top:819px;width:1200px;height:170px;background:var(--footer)}
  .footer-title{top:843px;font-size:18px;color:var(--white);letter-spacing:.3px}
  .footer-address{left:63px;top:877px;font-size:14.5px;line-height:19.6px;color:var(--white);letter-spacing:.3px}
  .social{position:absolute;left:419px;width:177px;height:33px;border:1px solid #1e1e1e;background:#333;
    display:flex;align-items:center;gap:12px;padding-left:6px;color:var(--white);font-size:17px}
  .social i{width:24px;height:24px;border-radius:50%;background:#9a9a9a}
  .copyright{right:61px;top:965px;font-size:11px;color:var(--white)}
</style>
</head>
<body>

<nav class="nav">
  <a class="current" href="#">HOME</a>
  <a href="#" style="left:182px">SERVICES</a>
  <a href="#" style="left:319px">PROJECTS</a>
  <a href="#" style="left:455px">TEAM</a>
  <a href="#" style="left:554px">ABOUT US</a>
  <a href="#" style="left:693px">CONTACT</a>
</nav>

<header>
  <div class="abs brand">
    <span class="brand-mark"></span>
    <span class="brand-name">Halvard Group</span>
  </div>
  <div class="abs phone">
    <svg width="36" height="40" viewBox="0 0 36 40" aria-hidden="true">
      <path d="M18 39 L12 30 A16 16 0 1 1 24 30 Z" fill="#f07a12"/>
      <circle cx="18" cy="17" r="12" fill="#f5a040"/>
      <path d="M12 12 q1-2 3-1 l2 3 q0 1-1 2 q1 3 4 4 q1-1 2-1 l3 2 q1 2-1 3 q-4 2-9-3 q-5-5-3-9z" fill="#fff"/>
    </svg>
    <span>555 218 9047</span>
  </div>
</header>

<section class="feature">
  <div class="abs feature-banner"></div>
  <h1 class="abs feature-title">Hospitality Management</h1>
  <p class="abs feature-text">Using proven strategies we maximize potential and produce profitable results for your hotel, just as we do with our own. Our management teams are empowered with the tools, training and resources to be successful.</p>
  <a class="abs btn-more" href="#">more
    <svg width="7" height="10" viewBox="0 0 7 10" aria-hidden="true"><path d="M0 0 L7 5 L0 10Z" fill="#2f2a26"/></svg>
  </a>
  <div class="abs slider-dots"><span></span><span></span><span></span><span></span></div>
  <div class="abs feature-photo" role="img" aria-label="Photo of a warmly lit hotel guest room with a bed, armchair and balcony doors"></div>
  <div class="abs photo-tab"></div>
</section>

<blockquote class="abs quote">“Halvard was founded on the principles of <strong>integrity, honesty, loyalty, and trust.</strong> These convictions embody our company at every level, and show in every action."</blockquote>
<p class="abs quote-author">-Soren Lindqvist, President and CEO</p>

<section class="abs info-band"></section>

<h2 class="col-title" style="left:66px">Welcome</h2>
<p class="abs welcome-text">Halvard Group is a fully integrated hospitality development, management, and investment firm. We strive for leadership in each of our segments by building quality assets, exacting high standards of customer service, and focusing on returns for our investors and partners.</p>
<a class="link-more" href="#" style="left:369px;top:774px">more</a>

<h2 class="col-title" style="left:491px">Our Services</h2>
<ul class="abs service-list">
  <li><svg width="6" height="9" viewBox="0 0 6 9" aria-hidden="true"><path d="M0 0 L6 4.5 L0 9Z" fill="#2f2a26"/></svg>Development Services</li>
  <li><svg width="6" height="9" viewBox="0 0 6 9" aria-hidden="true"><path d="M0 0 L6 4.5 L0 9Z" fill="#2f2a26"/></svg>Management Services</li>
  <li><svg width="6" height="9" viewBox="0 0 6 9" aria-hidden="true"><path d="M0 0 L6 4.5 L0 9Z" fill="#2f2a26"/></svg>Investment Services</li>
</ul>

<h2 class="col-title" style="left:823px">News</h2>
<article class="abs news-item" style="top:630px">
  <h3>Brookline Lodge &amp; Suites - Millford, OH</h3>
  <p>Appointed receiver of a 65 room hotel in April 2012.</p>
</article>
<a class="link-more" href="#" style="left:1067px;top:686px">more</a>
<div class="abs news-divider"></div>
<article class="abs news-item" style="top:728px">
  <h3>Harborview Stay &amp; Suites - Linden Commons, Oakridge, OH</h3>
  <p>New development opening fall 2012.</p>
</article>
<a class="link-more" href="#" style="left:1070px;top:792px">more</a>

<footer>
  <div class="abs footer"></div>
  <h2 class="abs footer-title" style="left:61px">HALVARD GROUP</h2>
  <address class="abs footer-address" style="font-style:normal">4810 Marlowe Park Dr.<br>#212, Fairhaven,<br>OH 45990<br>Ph: 555.218.9047</address>
  <h2 class="abs footer-title" style="left:422px;color:#d8d8d8">SOCIALISE WITH US</h2>
  <a class="social" href="#" style="top:880px"><i></i>Friendloop</a>
  <a class="social" href="#" style="top:924px"><i></i>Chirpline</a>
  <p class="abs copyright">Copyright 2012 Halvard Group. All rights reserved.</p>
</footer>

</body>
</html>
```